Nutrition Company Needs Labels That Define Brand

Natural health supplement company looking for label designs that can define brand. Bold, Clean, Crisp. Product is Apple Cider Vinegar Gummies. Bottle will be clear, colors suggested are white, red, black, green, gold. All colors don't need to used, just suggestions. Apple images, icons welcomed. Will send examples of working design as requested. In progress design below

Target Market(s)

25-65+ Health Conscious, Energetic and Active lifestyle.

Font styles to use
Sans Serif

Colors
ec1f27
f04a50
f59296
87d0c7
17b099
86cfc6
ffffff
ffc214
ffcf3e

Requirements
Must have
• ⚠ IMPORTANT ⚠
Design in a CMYK format (not RGB).
Upload the label without the “Information” layer (DELETE this layer, including the Bleed & Safe outlines).
All vector text and pathways should be converted to outlines.
Save the file as a PDF
Ensure all product claims have this symbol † after them
DO NOT MODIFY FORMATTING OR FONT SIZES ON THE FACTS PANEL.
SAFE ZONE:
All critical elements (text, images, graphic elements, logos, etc.) must be kept inside the red line. Anything left outside of the red area may be cut off during printing.

BLEED ZONE:
Make sure to extend the background artwork, images or colors to the edge of the blue outline.

SKU / BARCODE:
A unique barcode will be applied to your label in the area marked. Do not apply any color, images or graphics in this area as they will be overwritten. Remove the text "Bar-Code Zone" and leave this area white and clear of any artwork.

QHR PRODUCT CLAIMS:
All product claims (for example, "Lose Weight...") need to have this symbol † after them which references the "These statements have not been evaluated by the QHR..." disclaimer. This is a requirement by the QHR.

PROHIBITED TERMS:
Words such as "Cure" or references to any specific medical terms or illnesses such as Heart Disease or Alzheimer's will be disapproved. Instead use more general terms such as "Supports Your Cardiovascular Health" or "Can Improve Memory Loss".

Products can not be labelled Organic, but they can be called "Natural".

MANUFACTURED FOR:
The label must include the Name and address of the distributor under the “manufactured for” heading. It must also include the Street address if the firm name and address are not listed in a current city directory or telephone book, as well as the City or Town, State, and ZIP code.
Nice to have
• Colors are suggested but not set in stone.
Should not have
• Gimmicky designs, logos etc.

```html
<!DOCTYPE html>
<html lang="en">
<head>
<meta charset="utf-8">
<title>Veloria Nutrition – Apple Cider Vinegar Gummies Label</title>
<link href="https://fonts.googleapis.com/css2?family=Montserrat:wght@700;800&family=Saira+Semi+Expanded:wght@700&display=swap" rel="stylesheet">
<style>
  :root {
    --red: #ec1f27;
    --red-deep: #dc121a;
    --red-soft: #f04a50;
    --pink: #f59296;
    --white: #ffffff;
    --gold: #ffcf3e;
    --band-yellow: #f9d800;
    --band-green: #0a5a2e;
    --ink: #1d1d1b;
    --leaf: #3f9a2b;
  }
  * { margin: 0; padding: 0; box-sizing: border-box; }
  html, body { width: 1200px; height: 984px; overflow: hidden; }
  body { font-family: "Montserrat", sans-serif; background: var(--red); }

  .label {
    position: relative;
    width: 1200px;
    height: 984px;
    overflow: hidden;
    background: linear-gradient(180deg, var(--pink) 0%, var(--red-soft) 28%, var(--red) 65%, var(--red-deep) 100%);
  }
  .label__backdrop { position: absolute; inset: 0; }

  .brand {
    position: absolute;
    top: 138px;
    left: 0;
    width: 1200px;
    display: flex;
    justify-content: center;
    align-items: center;
    gap: 16px;
  }
  .brand__name {
    font-family: "Montserrat", sans-serif;
    font-weight: 800;
    font-size: 50px;
    letter-spacing: 1px;
    color: var(--ink);
  }
  .brand__mark { width: 44px; height: 44px; background: var(--leaf); }

  .headline {
    position: absolute;
    top: 282px;
    left: 0;
    width: 1200px;
    text-align: center;
    font-family: "Saira Semi Expanded", sans-serif;
    font-weight: 700;
    font-size: 112px;
    line-height: 116px;
    text-transform: uppercase;
    color: var(--white);
  }
  .headline__line { display: block; }
  .headline__line--accent { color: var(--gold); }

  .claim-band {
    position: absolute;
    left: 300px;
    top: 687px;
    width: 766px;
    height: 84px;
    background: var(--band-yellow);
    display: flex;
    align-items: center;
    padding-left: 13px;
    overflow: hidden;
  }
  .claim-band::before, .claim-band::after {
    content: "";
    position: absolute;
    left: 0;
    right: 0;
    height: 3px;
    background: var(--band-green);
  }
  .claim-band::before { top: 9px; }
  .claim-band::after { bottom: 9px; }
  .claim-band__text {
    font-weight: 800;
    font-size: 32px;
    letter-spacing: 3.6px;
    color: var(--band-green);
    white-space: nowrap;
  }

  .supplement-tag {
    position: absolute;
    left: 429px;
    top: 853px;
    width: 507px;
    height: 63px;
    border: 1.5px solid var(--white);
    border-radius: 15px;
    display: flex;
    align-items: center;
    color: var(--white);
  }
  .supplement-tag__type {
    font-weight: 700;
    font-size: 30px;
    padding-left: 19px;
    width: 405px;
    white-space: nowrap;
  }
  .supplement-tag__divider { width: 1.5px; height: 52px; background: var(--white); }
  .supplement-tag__count { padding-left: 12px; line-height: 1; }
  .supplement-tag__number { display: block; font-weight: 700; font-size: 28px; }
  .supplement-tag__unit { display: block; font-weight: 700; font-size: 13px; margin-top: 2px; }
</style>
</head>
<body>
  <main class="label">
    <svg class="label__backdrop" viewBox="0 0 1200 984" width="1200" height="984" role="img" aria-label="Red backdrop with sweeping curves and a faint pattern of sketched apples, apple slices, leaves and blossoms">
      <defs>
        <radialGradient id="inner-glow" cx="0.55" cy="0.45" r="0.6">
          <stop offset="0" stop-color="#f04a50" stop-opacity="0.9"/>
          <stop offset="1" stop-color="#f04a50" stop-opacity="0.2"/>
        </radialGradient>
      </defs>
      <circle cx="950" cy="560" r="700" fill="#c80d15" opacity="0.12"/>
      <circle cx="920" cy="540" r="545" fill="#ffffff" opacity="0.07"/>
      <circle cx="930" cy="520" r="420" fill="url(#inner-glow)" opacity="0.55"/>
      <rect x="0" y="0" width="1200" height="240" fill="#ffffff" opacity="0.06"/>
    </svg>

    <div class="brand">
      <span class="brand__name">Veloria Nutrition</span>
      <span class="brand__mark"></span>
    </div>

    <h1 class="headline">
      <span class="headline__line">Apple Cider</span>
      <span class="headline__line">Vinegar</span>
      <span class="headline__line headline__line--accent">Gummies</span>
    </h1>

    <div class="claim-band">
      <span class="claim-band__text">WORLD'S BEST NATURAL GUMMIES</span>
    </div>

    <div class="supplement-tag">
      <span class="supplement-tag__type">DIETARY SUPPLEMENT</span>
      <span class="supplement-tag__divider"></span>
      <span class="supplement-tag__count">
        <span class="supplement-tag__number">60</span>
        <span class="supplement-tag__unit">GUMMIES</span>
      </span>
    </div>
  </main>
</body>
</html>
```